Business Cards for, Telumo Varisenka - Spending Planner, employed by Clear Path Budget Coach - new business based in Brisbane Australia.

Small Business providing 'Spending Planing' services. Helping people, families, homes, businesses achieve their budgeting goals.

Motto: Plan Wisely Build Freedom

Final design should communicate financial freedom and strong positive growth.

Target Market(s)

Working Families, Finance, Retail,

Industry/Entity Type

Finance

Contact Information for Business Card

Name, Company Title
Mobile details, Email details

Logo Text

Clear Path Budget Coach - Plan Wisely Build Freedom

Font styles to use
Serif

Requirements
Must have
• Easy to read
Nice to have
• Modern Looking
Should not have
• Not too confusing to understand

```html
<!DOCTYPE html>
<html lang="en">
<head>
<meta charset="utf-8">
<title>Clear Path Budget Coach – Business Card</title>
<link rel="stylesheet" href="https://fonts.googleapis.com/css2?family=Roboto+Condensed:ital,wght@0,300;0,400;0,700;1,700&display=swap">
<style>
  :root {
    --gold: #c98f34;
    --orange: #f7a23c;
    --ink: #0d0d0d;
    --paper: #ffffff;
    --backdrop: #e9e7e3;
  }
  * { margin: 0; padding: 0; box-sizing: border-box; }
  html, body {
    width: 960px; height: 1200px; overflow: hidden;
    background: var(--backdrop);
    font-family: "Roboto Condensed", "Arial Narrow", sans-serif;
  }
  .card {
    position: absolute; left: 40px; top: 350px;
    width: 880px; height: 500px;
    background: var(--paper);
    box-shadow: 0 10px 30px rgba(0,0,0,.18);
    overflow: hidden;
  }
  .card-art { position: absolute; inset: 0; width: 880px; height: 500px; }
  .company {
    position: absolute; left: 71px; top: 40px;
    font-weight: 700; font-size: 56px; line-height: 1;
    color: var(--gold); letter-spacing: .5px;
  }
  .person-name {
    position: absolute; left: 69px; top: 124px;
    font-weight: 700; font-style: italic; font-size: 42px; line-height: 1;
    color: var(--ink); letter-spacing: 1px; text-transform: uppercase;
  }
  .person-role {
    position: absolute; left: 70px; top: 174px;
    font-weight: 300; font-size: 31px; line-height: 1;
    color: var(--ink); letter-spacing: 1px; text-transform: uppercase;
  }
  .contact {
    position: absolute; left: 69px;
    display: flex; align-items: center; gap: 10px;
    font-weight: 300; font-size: 28px; line-height: 1; color: var(--ink);
  }
  .contact.phone { top: 230px; }
  .contact.email { top: 294px; }
  .contact-icon {
    width: 50px; height: 50px; border-radius: 4px;
    background: var(--orange);
    display: flex; align-items: center; justify-content: center;
  }
  .motto {
    position: absolute; left: 0; right: 0; top: 425px;
    text-align: center; color: var(--paper);
    font-size: 47px; line-height: 1; letter-spacing: 1px; text-transform: uppercase;
  }
  .motto-light { font-weight: 300; }
  .motto-bold { font-weight: 700; }
</style>
</head>
<body>
  <article class="card">
    <svg class="card-art" viewBox="0 0 880 500" aria-hidden="true">
      <path d="M0 352 C250 428 600 434 880 304 V500 H0 Z" fill="var(--gold)"/>
      <path d="M0 352 C250 428 600 434 880 304 V250 C650 396 320 430 0 352 Z" fill="var(--ink)"/>
      <path d="M330 422 C560 416 730 374 836 304" fill="none" stroke="var(--gold)" stroke-width="3"/>
      <path d="M842 298 L818 304 L830 316 Z" fill="var(--gold)"/>
    </svg>

    <div class="company">Clear Path Budget Coach</div>
    <div class="person-name">Telumo Varisenka</div>
    <div class="person-role">Spending Planner</div>

    <div class="contact phone">
      <span class="contact-icon">
        <svg width="32" height="32" viewBox="0 0 24 24" aria-hidden="true">
          <path fill="#fff" d="M6.6 10.8a15.1 15.1 0 0 0 6.6 6.6l2.2-2.2a1 1 0 0 1 1-.25 11.4 11.4 0 0 0 3.6.57 1 1 0 0 1 1 1V20a1 1 0 0 1-1 1A17 17 0 0 1 3 4a1 1 0 0 1 1-1h3.5a1 1 0 0 1 1 1c0 1.25.2 2.45.57 3.57a1 1 0 0 1-.25 1z"/>
        </svg>
      </span>
      <span class="contact-text">+61 400 555 019</span>
    </div>

    <div class="contact email">
      <span class="contact-icon">
        <svg width="40" height="40" viewBox="0 0 24 24" aria-hidden="true">
          <text x="12" y="19" text-anchor="middle" font-family="Roboto Condensed, sans-serif" font-weight="400" font-size="22" fill="#fff">@</text>
        </svg>
      </span>
      <span class="contact-text">telumo@clearpathbc.com</span>
    </div>

    <div class="motto"><span class="motto-light">Plan Wisely</span> <span class="motto-bold">Build Freedom</span></div>
  </article>
</body>
</html>
```